KPVT

We want to design our company brochure. We are a newly established ship management company in Singapore. We manage a fleet of bulk carrier and car carriers. Our job is to run the ships economically and efficiently on behalf of owners of the vessel.
Updates

Project Deadline Extended
Reason: We are not satisfied by the designs as yet. Hence, we are extending the deadline further by 7 days.

Project Deadline Extended
Reason: No designs are up to our expectations

Project Deadline Extended

Target Market(s)

Our target market is various ship owners based all over the world especially in Japan and Europe. These ship owners are looking for third party managers to run their ships economically and efficiently.

Industry/Entity Type

It Company

Colors
32b7a4
33a6d7
00a88f
3276b5
0692cd
86cae6
86cfc6
ebf7f9
edf2f7

Requirements
Must have
• The brochure must have four pages (in form of a folder) with static information, photographs etc with a pocket designed inside to keep printed sheets containing dynamic information.
Write up on our company is attached herewith and also some photographs depicting our ships, crew and the training center.
Information for dynamic sheets is attached in a separate sheets.

```html
<!DOCTYPE html>
<html lang="en">
<head>
<meta charset="utf-8">
<title>KPVT Brochure Spread</title>
<link href="https://fonts.googleapis.com/css2?family=Open+Sans:wght@400;600;700;800&display=swap" rel="stylesheet">
<style>
:root{
  --canvas:#e4e4e4;
  --page-top:#f4f4f4;
  --page-bottom:#d8d8d8;
  --band:#4a4a4a;
  --tab:#5e5e5e;
  --text:#3a3a3a;
  --text-soft:#555555;
  --white:#ffffff;
  --rule:#9a9a9a;
}
*{margin:0;padding:0;box-sizing:border-box}
html,body{width:1200px;height:847px;overflow:hidden}
body{background:var(--canvas);font-family:"Open Sans",Arial,sans-serif;color:var(--text);position:relative}
.spread{position:absolute;left:60px;top:41px;width:1080px;height:764px;box-shadow:0 10px 30px rgba(0,0,0,.18)}
.page{position:absolute;top:0;width:540px;height:764px;background:linear-gradient(180deg,var(--page-top),var(--page-bottom));overflow:hidden}
.page--left{left:0}
.page--right{left:540px}
.top-band{position:absolute;left:0;top:0;width:540px;height:40px}
.section-title{position:absolute;font-weight:800;font-size:21px;letter-spacing:.5px;color:var(--text)}
.section-title::before{content:"";position:absolute;left:-42px;top:4px;width:32px;height:20px;background:var(--band)}
.about-text{position:absolute;left:40px;top:88px;width:272px;font-size:9.4px;line-height:1.4;color:var(--text-soft);text-align:justify}
.about-text p{margin-bottom:8px}
.photo{position:absolute;border:3px solid var(--white);box-shadow:0 1px 4px rgba(0,0,0,.25)}
.photo-col .photo{left:335px;width:180px;height:148px}
.tab{position:absolute;height:26px;background:var(--tab);color:var(--white);font-size:12.5px;font-weight:700;letter-spacing:.6px;padding:4px 18px 0 18px}
.services{position:absolute;left:40px;top:452px;width:270px;list-style:none}
.services > li{display:flex;gap:12px;font-size:12.5px;font-weight:700;margin-bottom:12px;align-items:flex-start}
.sublist{position:absolute;left:60px;top:560px;width:250px;list-style:none;border-left:1px solid var(--rule);padding-left:14px}
.sublist li{display:flex;gap:8px;font-size:11px;font-weight:700;margin-bottom:6px;align-items:center}
.tick{flex:none;width:14px;height:12px;margin-top:2px}
.divider{position:absolute;left:322px;top:410px;width:1px;height:300px;background:var(--rule)}
.initiatives{position:absolute;left:40px;top:340px;width:470px;list-style:none}
.initiatives li{display:flex;gap:9px;font-size:10.6px;line-height:1.45;margin-bottom:6px;color:var(--text)}
.commitment{position:absolute;left:30px;top:520px;width:510px;height:210px;background:var(--tab);border-radius:18px 0 0 0}
.commitment h2{position:absolute;left:24px;top:22px;color:var(--white);font-weight:800;font-size:21px;letter-spacing:.5px}
.commitment p{position:absolute;left:24px;top:62px;width:240px;color:#e9e9e9;font-size:11px;line-height:1.5;text-align:justify}
.commitment .photo{left:270px;top:20px;width:200px;height:160px}
</style>
</head>
<body>
<div class="spread">
  <section class="page page--left">
    <svg class="top-band" viewBox="0 0 540 40" aria-hidden="true">
      <polygon points="0,10 540,10 540,30 0,30" fill="var(--band)"/>
    </svg>
    <h2 class="section-title" style="left:52px;top:52px">ABOUT US</h2>
    <div class="about-text">
      <p>Kinvara Pacific Vessel Technics Pte. Ltd. established in Singapore in 2012 as a Ship Management company with a clear objective to provide quality service to the Ship Owners while maintaining a fine balance and harmony between cost, efficient operation and giving a humane touch to the Ship Management.</p>
      <p>With this philosophy Kinvara Pacific Vessel Technics Pte. Ltd was formed and was chosen as a dependable ally by Harbourline Group who have trusted us for the upkeep and safe operation of their ships for majority of their existing fleet and all new building vessels.</p>
      <p>We have a vision – to contribute to the ship management business its lost pride and glory by running Clean, Safe and Happy Ships ethically.</p>
      <p>Company is headed by Mr. Arjun Mehta who has more than 20 years of sea and shore based experience in various positions in the Shipping industry with majority of time spent ashore in key management position. KPVT is his brainchild and a reflection of his youthful and energetic persona. Like minded professionals were chosen right from the inception who have become the corner stones of the organization to build a strong yet dynamic entity.</p>
    </div>
    <div class="photo-col">
      <div class="photo" style="top:52px;background:linear-gradient(180deg,#a9c6de 0%,#dfe8ef 45%,#f4f6f8 60%,#6f8ea8 100%)" role="img" aria-label="Car carrier vessel at sea"></div>
      <div class="photo" style="top:212px;background:linear-gradient(180deg,#f3f3f3 0%,#e5e5e5 35%,#c23a2e 55%,#a8261d 80%,#d9d9d9 100%)" role="img" aria-label="Crew in red survival suits on deck"></div>
      <div class="photo" style="top:372px;background:linear-gradient(180deg,#b8c7d4 0%,#d7dee5 50%,#5a3a36 62%,#8a2b22 70%,#7f95a6 100%)" role="img" aria-label="Bulk carrier anchored at sea"></div>
      <div class="photo" style="top:532px;background:linear-gradient(180deg,#c9c4b0 0%,#9f9a86 40%,#e07a2e 60%,#6e6b63 100%)" role="img" aria-label="Crew in safety gear inside cargo hold"></div>
    </div>
    <div class="tab" style="left:0;top:410px;width:200px">SERVICES OFFERED</div>
    <div class="divider"></div>
    <ul class="services">
      <li><svg class="tick" viewBox="0 0 14 12" aria-hidden="true"><path d="M1 6 L5 10 L13 1" fill="none" stroke="var(--text)" stroke-width="1.6"/></svg>Ship Management</li>
      <li><svg class="tick" viewBox="0 0 14 12" aria-hidden="true"><path d="M1 6 L5 10 L13 1" fill="none" stroke="var(--text)" stroke-width="1.6"/></svg>Technical Solutions</li>
      <li style="padding-left:26px">An array of technical solutions for the shipping world</li>
    </ul>
    <ul class="sublist">
      <li><svg class="tick" viewBox="0 0 14 12" aria-hidden="true"><path d="M1 6 L5 10 L13 1" fill="none" stroke="var(--text)" stroke-width="1.6"/></svg>Technical Consultancy</li>
      <li><svg class="tick" viewBox="0 0 14 12" aria-hidden="true"><path d="M1 6 L5 10 L13 1" fill="none" stroke="var(--text)" stroke-width="1.6"/></svg>New Building Supervision</li>
      <li><svg class="tick" viewBox="0 0 14 12" aria-hidden="true"><path d="M1 6 L5 10 L13 1" fill="none" stroke="var(--text)" stroke-width="1.6"/></svg>Pre-Purchase Surveys</li>
      <li><svg class="tick" viewBox="0 0 14 12" aria-hidden="true"><path d="M1 6 L5 10 L13 1" fill="none" stroke="var(--text)" stroke-width="1.6"/></svg>On-Site Supervision</li>
      <li><svg class="tick" viewBox="0 0 14 12" aria-hidden="true"><path d="M1 6 L5 10 L13 1" fill="none" stroke="var(--text)" stroke-width="1.6"/></svg>Dry Docking</li>
      <li><svg class="tick" viewBox="0 0 14 12" aria-hidden="true"><path d="M1 6 L5 10 L13 1" fill="none" stroke="var(--text)" stroke-width="1.6"/></svg>Condition Surveys</li>
      <li><svg class="tick" viewBox="0 0 14 12" aria-hidden="true"><path d="M1 6 L5 10 L13 1" fill="none" stroke="var(--text)" stroke-width="1.6"/></svg>Port Captaincy</li>
    </ul>
  </section>

  <section class="page page--right">
    <svg class="top-band" viewBox="0 0 540 40" aria-hidden="true">
      <polygon points="0,10 540,10 540,30 0,30" fill="var(--band)"/>
    </svg>
    <div class="photo" style="left:30px;top:48px;width:480px;height:250px;background:linear-gradient(90deg,#dcd6cf 0%,#f1ece6 40%,#c9b7a6 60%,#8b7466 80%,#cfc8c2 100%)" role="img" aria-label="Representative office corridor with company sign"></div>
    <div class="tab" style="left:0;top:310px;width:150px">INITIATIVES</div>
    <ul class="initiatives">
      <li><svg class="tick" viewBox="0 0 14 12" aria-hidden="true"><path d="M1 6 L5 10 L13 1" fill="none" stroke="var(--text)" stroke-width="1.6"/></svg>Started own in house training institute in Manila to train our staff and keep them abreast of new developments in shipping industry.</li>
      <li><svg class="tick" viewBox="0 0 14 12" aria-hidden="true"><path d="M1 6 L5 10 L13 1" fill="none" stroke="var(--text)" stroke-width="1.6"/></svg>ECDIS installation started on board in order to ensure smooth transition to paperless navigation with proper training to ship staff in our training center.</li>
      <li><svg class="tick" viewBox="0 0 14 12" aria-hidden="true"><path d="M1 6 L5 10 L13 1" fill="none" stroke="var(--text)" stroke-width="1.6"/></svg>Commenced internet facility on board all our vessels. 20 mb data being given free to each crew every month.</li>
      <li><svg class="tick" viewBox="0 0 14 12" aria-hidden="true"><path d="M1 6 L5 10 L13 1" fill="none" stroke="var(--text)" stroke-width="1.6"/></svg>Special emphasis on crew welfare with supply of fitness and entertainment equipment on board.</li>
      <li><svg class="tick" viewBox="0 0 14 12" aria-hidden="true"><path d="M1 6 L5 10 L13 1" fill="none" stroke="var(--text)" stroke-width="1.6"/></svg>Assistance like free telephone cards, internet cards, cash donation provided to staff in case of a natural calamity in home country.</li>
    </ul>
    <div class="commitment">
      <h2>COMMITMENT</h2>
      <p>The company believes that good training, motivation and emphasis on human values are essential for long term success. Consequently, the company is committed to providing an ideal working environment both in its offices and on ships.</p>
      <div class="photo" style="background:linear-gradient(180deg,#c4d3e0 0%,#e3e9ee 40%,#2c2c2c 55%,#b3302a 72%,#8f8a80 100%)" role="img" aria-label="Bulk carrier berthed at a port with cranes"></div>
    </div>
  </section>
</div>
</body>
</html>
```